Broschüren-Design für Pizzalieferdienst
Zielgruppe
Wir sind ein Pizzalieferdienst in Südtirol.
Aufgabenstellung
Es soll eine Broschüre werden, die als Speisekarte dient und wie man sie nicht oft sieht. Ausgefallene Ideen werden bevorzugt.
Um die maximale Kreativität zu fördern wird lediglich das Logo und die Schriftart vorgegeben.
Viel Spass an alle Teilnehmer!

```html
<!DOCTYPE html>
<html lang="de">
<head>
<meta charset="utf-8">
<title>Pizzavolo – Speisekarte</title>
<link href="https://fonts.googleapis.com/css2?family=Lobster&family=Open+Sans:wght@400;700&display=swap" rel="stylesheet">
<style>
  :root {
    --stage: #c9cdd0;
    --maroon: #4a1117;
    --maroon-light: #6a1a20;
    --maroon-dark: #2e080c;
    --paper: #ffffff;
    --dough: #d9a35a;
    --basil: #3f7a2a;
    --garlic: #c98aa0;
  }
  * { margin: 0; padding: 0; box-sizing: border-box; }
  html, body { width: 1200px; height: 1200px; overflow: hidden; }
  body { background: var(--stage); position: relative; font-family: "Open Sans", Arial, sans-serif; color: var(--paper); }

  .page {
    position: absolute; top: 368px; height: 470px; overflow: hidden;
    background:
      radial-gradient(ellipse at 40% 35%, var(--maroon-light) 0%, transparent 60%),
      linear-gradient(160deg, var(--maroon) 0%, var(--maroon-dark) 100%);
  }
  .cover { left: 76px; width: 334px; }
  .spread-left { left: 468px; width: 333px; }
  .spread-right { left: 801px; width: 333px; border-left: 1px solid rgba(0,0,0,.35); }

  .photo { position: absolute; }
  .photo-round { border-radius: 50%; }

  /* Cover */
  .brand-name {
    position: absolute; top: 12px; left: 0; right: 0; text-align: center;
    font-family: "Open Sans", Arial, sans-serif; font-weight: 700; font-size: 17px; letter-spacing: .5px; color: var(--paper);
  }
  .cover-pizza { left: 69px; top: 117px; width: 210px; height: 210px;
    background: radial-gradient(circle, #e8c27a 0%, var(--dough) 70%, #a8672c 100%); }
  .cover-herbs { left: 6px; top: 318px; width: 70px; height: 65px; border-radius: 40%;
    background: radial-gradient(circle, #7a9b3a 0%, rgba(122,155,58,0) 70%); }
  .cover-pasta { left: -20px; top: 376px; width: 90px; height: 94px;
    background: radial-gradient(circle, #c8783a 0%, #efe6da 55%, #ffffff 70%); }
  .cover-spices { right: 0; top: 398px; width: 72px; height: 72px; border-radius: 30% 0 0 0;
    background: radial-gradient(circle at 40% 50%, #8e8a80 0%, #4a3a2e 55%, rgba(74,58,46,0) 80%); }
  .contact { position: absolute; left: 0; right: 0; top: 426px; text-align: center;
    font-family: "Lobster", cursive; font-size: 12px; line-height: 16px; }
  .contact svg { vertical-align: -2px; margin-right: 3px; }

  /* Spread headings */
  .title { position: absolute; left: 0; right: 0; top: 2px; text-align: center;
    font-family: "Lobster", cursive; font-size: 52px; line-height: 60px; color: var(--paper); }
  .banner { position: absolute; height: 34px; background: var(--paper); white-space: nowrap;
    font-family: "Lobster", cursive; color: var(--maroon); font-size: 21px; line-height: 34px; }
  .banner-klassisch { left: 0; top: 98px; width: 160px; padding-left: 7px;
    clip-path: polygon(0 0, 100% 0, 93% 50%, 100% 100%, 0 100%); }
  .banner-scharf { right: 0; top: 18px; width: 172px; padding-left: 24px;
    clip-path: polygon(0 0, 100% 0, 100% 100%, 0 100%, 8% 50%); }
  .banner-spezial { left: 0; top: 269px; width: 163px; padding-left: 6px;
    clip-path: polygon(0 0, 100% 0, 92% 50%, 100% 100%, 0 100%); }

  .klassisch-pizza { left: 158px; top: 68px; width: 110px; height: 86px;
    background: radial-gradient(ellipse, #e9c77e 0%, #c9733a 75%, #8a3a1a 100%); }
  .bottom-pizza { left: 66px; top: 382px; width: 199px; height: 199px;
    background: radial-gradient(circle, #f1dcae 0%, #e1b26a 65%, #b2723a 100%); }
  .chilis { left: 68px; top: 12px; width: 88px; height: 60px; border-radius: 45%;
    background: radial-gradient(ellipse, #c21a1e 0%, #8c1014 55%, rgba(140,16,20,0) 75%); }
  .basil { left: -8px; top: 390px; width: 120px; height: 90px; border-radius: 50% 50% 0 0;
    background: radial-gradient(ellipse at 40% 55%, #4f8a32 0%, var(--basil) 55%, rgba(63,122,42,0) 78%); }
  .garlic { right: -6px; top: 392px; width: 110px; height: 84px; border-radius: 50% 50% 0 0;
    background: radial-gradient(ellipse at 45% 55%, #f1e4e6 0%, var(--garlic) 55%, rgba(201,138,160,0) 78%); }

  /* Menu items */
  .item { position: absolute; }
  .spread-left .item { left: 20px; right: 47px; }
  .spread-right .item { left: 22px; right: 44px; }
  .item-row { display: flex; align-items: baseline; font-family: "Lobster", cursive; font-size: 10.5px; line-height: 12px; }
  .item-leader { flex: 1; border-bottom: 1.5px dotted var(--paper); margin: 0 3px; transform: translateY(-2px); }
  .item-desc { font-family: Arial, Helvetica, sans-serif; font-size: 5.6px; line-height: 7px; max-width: 150px; color: #f2e6e6; }
</style>
</head>
<body>

  <section class="page cover">
    <div class="brand-name">PIZZAVOLO</div>
    <div class="photo photo-round cover-pizza" role="img" aria-label="Geschnittene Pizza mit Oliven, Paprika und Basilikum, mit Mehl bestäubt"></div>
    <div class="photo cover-herbs" role="img" aria-label="Basilikum, Knoblauch und Chilis"></div>
    <div class="photo photo-round cover-pasta" role="img" aria-label="Teller mit Spaghetti"></div>
    <div class="photo cover-spices" role="img" aria-label="Schälchen mit Salz, Pfeffer und Paprikapulver"></div>
    <div class="contact">
      <div><svg width="10" height="10" viewBox="0 0 24 24"><path fill="#fff" d="M6.6 10.8a15.1 15.1 0 0 0 6.6 6.6l2.2-2.2c.3-.3.7-.4 1-.2 1.1.4 2.3.6 3.6.6.6 0 1 .4 1 1V20c0 .6-.4 1-1 1A17 17 0 0 1 3 4c0-.6.4-1 1-1h3.5c.6 0 1 .4 1 1 0 1.3.2 2.5.6 3.6.1.3 0 .7-.2 1z"/></svg>+39 0471 555 010</div>
      <div><svg width="12" height="9" viewBox="0 0 24 18"><rect x="1" y="1" width="22" height="16" fill="none" stroke="#fff" stroke-width="1.6"/><path d="M1 1l11 9 11-9" fill="none" stroke="#fff" stroke-width="1.6"/></svg>info@pizzavolo.example</div>
    </div>
  </section>

  <section class="page spread-left">
    <h1 class="title">Pizza</h1>
    <div class="banner banner-klassisch">Pizza Klassisch</div>
    <div class="photo photo-round klassisch-pizza" role="img" aria-label="Pizza mit Salami und Basilikum"></div>

    <div class="item" style="top:160px"><div class="item-row"><span>Pizza Marinara</span><span class="item-leader"></span><span>5,80 €</span></div><p class="item-desc">(Tomatensauce, Knoblauch, Origano)</p></div>
    <div class="item" style="top:181px"><div class="item-row"><span>Pizza Margherita</span><span class="item-leader"></span><span>6,50 €</span></div><p class="item-desc">(Tomatensauce, Mozzarella, Origano)</p></div>
    <div class="item" style="top:201px"><div class="item-row"><span>Pizza Napoli</span><span class="item-leader"></span><span>7,60 €</span></div><p class="item-desc">(Tomatensauce, Mozzarella, Sardellen, Origano)</p></div>
    <div class="item" style="top:222px"><div class="item-row"><span>Pizza Schinken</span><span class="item-leader"></span><span>7,60 €</span></div><p class="item-desc">(Tomatensauce, Mozzarella, Schinken, Origano)</p></div>
    <div class="item" style="top:243px"><div class="item-row"><span>Pizza Thunfisch-Zwiebel</span><span class="item-leader"></span><span>8,90 €</span></div><p class="item-desc">(Tomatensauce, Mozzarella, Thunfisch, Zwiebel, Origano)</p></div>
    <div class="item" style="top:272px"><div class="item-row"><span>Pizza Schinken-Pilze</span><span class="item-leader"></span><span>8,70 €</span></div><p class="item-desc">(Tomatensauce, Mozzarella, Schinken, Champignons, Origano)</p></div>
    <div class="item" style="top:300px"><div class="item-row"><span>Pizza Capricciosa</span><span class="item-leader"></span><span>9,20 €</span></div><p class="item-desc">(Tomatensauce, Mozzarella, Schinken, Champignons, Artischocken, Oliven, Origano)</p></div>
    <div class="item" style="top:329px"><div class="item-row"><span>Calzone</span><span class="item-leader"></span><span>8,70 €</span></div><p class="item-desc">(Mozzarella, Schinken, Champignons, Origano, separate Tomatensoße)</p></div>

    <div class="photo photo-round bottom-pizza" role="img" aria-label="Pizza mit Tomaten und roter Paprika"></div>
  </section>

  <section class="page spread-right">
    <div class="photo chilis" role="img" aria-label="Bündel roter Chilischoten"></div>
    <div class="banner banner-scharf">Pizza Scharf</div>

    <div class="item" style="top:77px"><div class="item-row"><span>Pizza Scharfe Salami</span><span class="item-leader"></span><span>7,60 €</span></div><p class="item-desc" style="max-width:170px">Tomatensauce, Mozzarella, scharfe Salami, Origano)</p></div>
    <div class="item" style="top:98px"><div class="item-row"><span>Pizza Arrabiata</span><span class="item-leader"></span><span>8,70 €</span></div><p class="item-desc">(Tomatensauce, Mozzarella, scharfe Salami, Knoblauch, Parmesan)</p></div>
    <div class="item" style="top:127px"><div class="item-row"><span>Pizza Amerikanisch</span><span class="item-leader"></span><span>8,70 €</span></div><p class="item-desc" style="max-width:170px">(Tomatensauce, Mozzarella, scharfe Salami, gegrillte Peperoni, Peperoncino, Origano)</p></div>
    <div class="item" style="top:154px"><div class="item-row"><span>Pizza Teufel</span><span class="item-leader"></span><span>9,20 €</span></div><p class="item-desc">(Tomatensauce, Mozzarella, scharfe Salami, Peperonata, Peperoni Lombardi, Oliven, Origano)</p></div>
    <div class="item" style="top:184px"><div class="item-row"><span>Pizza Feuerdrache</span><span class="item-leader"></span><span>9,20 €</span></div><p class="item-desc">(Tomatensauce, Mozzarella, scharfe Salami, Peperoni Veneti, Sardellen, Origano)</p></div>
    <div class="item" style="top:211px"><div class="item-row"><span>Pizza Bauern</span><span class="item-leader"></span><span>9,20 €</span></div><p class="item-desc" style="max-width:160px">(Tomatensauce, Mozzarella, scharfe Salami, Spiegelei, Speck, Origano)</p></div>

    <div class="banner banner-spezial">Pizza Spezial</div>

    <div class="item" style="top:318px"><div class="item-row"><span>Pizza Bolide</span><span class="item-leader"></span><span>9,20 €</span></div><p class="item-desc">(Tomatensauce, Mozzarella, ungarische Salami, Peperonata, Artischocken, Origano)</p></div>
    <div class="item" style="top:346px"><div class="item-row"><span>Pizza Body Builder</span><span class="item-leader"></span><span>9,20 €</span></div><p class="item-desc" style="max-width:180px">(Tomatensauce, Mozzarella, Speck, Zwiebel, Peperonata, Origano)</p></div>
    <div class="item" style="top:367px"><div class="item-row"><span>Pizza Millander</span><span class="item-leader"></span><span>9,70 €</span></div><p class="item-desc" style="max-width:180px">(Tomatensauce, Mozzarella, Speck, Kaminwurze, Zwiebel, Origano)</p></div>

    <div class="photo basil" role="img" aria-label="Frische Basilikumblätter"></div>
    <div class="photo garlic" role="img" aria-label="Knoblauchknollen"></div>
  </section>

</body>
</html>
```